Asia based real estate financing firm needs and AWESOME design for a biz card -Harbor Lending Circle

Looking for a stylish, & corporate-looking business card for a real estate financing brokerage firm in Asia, offering global mortgage loans. I uploaded our current logos. We would like to add a splash of color (perhaps the house icon) or any other suggestions are open. For the winning designer, we have a lot of work! Thanks and best of luck!

Target Market(s)

Real estate investors globally. We want to look more like a BANK and NOT a real estate company. Please don't play up on a "house" design.

Industry/Entity Type

Banking

Contact Information for Business Card

Harbor Lending Circle
Peter Wilks
Co-Founder | Partner

14 Cassia Lane, Suite 310
Singapore 047219
www.hlc-example.asia
peterwilks@hlc-example.asia
+65 555-0142
WeChat: peterwilks

Colors

Designer to choose colors to be used in the design.

Requirements
Must have
• Must have the standard business requirements for a card; name, address, email, etc
• Can be horizontal or vertical.
Nice to have
• It would be great to see some sort of variation to the logo with a pop of color. Red is good as we're in Asia, however, other options work as well.
• Our tag line is - Borderless mortgages. It doesn't have to be on the card but might be nice.
• I'd like to start seeing our tagline within the cards as well. - Borderless mortgages.
• Also, please add our location. The location for this card is Singapore so perhaps it can be highlighted or emphasised in some way.
• Singapore | Hong Kong | Shanghai | Manila
• As we will soon open an office in Shanghai, having an option for both languages would be great.
Should not have
• I'm exceited and open to your creativity ... knock it out of the park!

```html
<!DOCTYPE html>
<html lang="en">
<head>
<meta charset="utf-8">
<title>Harbor Lending Circle — Business Card</title>
<link rel="stylesheet" href="https://fonts.googleapis.com/css2?family=Roboto:wght@400;500;700&display=swap">
<style>
  :root {
    --page-bg: #dedede;
    --card-white: #ffffff;
    --card-black: #000000;
    --brand-red: #c0161a;
    --text-grey: #4a4a4a;
  }
  * { margin: 0; padding: 0; box-sizing: border-box; }
  html, body {
    width: 1125px;
    height: 1200px;
    overflow: hidden;
    background: var(--page-bg);
    font-family: "Roboto", Arial, sans-serif;
  }
  .card {
    position: absolute;
    left: 171px;
    width: 826px;
    height: 472px;
    overflow: hidden;
  }
  .card-front { top: 106px; background: var(--card-white); }
  .card-back  { top: 639px; background: var(--card-black); }
  .accent-band {
    position: absolute;
    left: 0; bottom: 0;
    width: 100%;
    height: 15px;
    background: var(--brand-red);
  }
  .corner-mark {
    position: absolute;
    right: 150px;
    bottom: 19px;
    width: 18px;
    height: 18px;
    background: var(--brand-red);
  }
  .brand-name {
    position: absolute;
    color: var(--brand-red);
    font-weight: 500;
    white-space: nowrap;
  }
  .card-front .brand-name {
    left: 60px;
    top: 118px;
    font-size: 36px;
    letter-spacing: 0.5px;
  }
  .card-back .brand-name {
    left: 0;
    width: 100%;
    top: 185px;
    text-align: center;
    font-size: 52px;
    letter-spacing: 1px;
  }
  .address {
    position: absolute;
    left: 60px;
    top: 243px;
    font-size: 20px;
    line-height: 26px;
    color: var(--text-grey);
  }
  .contact-list {
    position: absolute;
    left: 60px;
    top: 306px;
    list-style: none;
    font-size: 20px;
    color: var(--text-grey);
  }
  .contact-list li {
    display: flex;
    align-items: center;
    height: 26.5px;
  }
  .contact-icon {
    width: 18px;
    height: 18px;
    margin-right: 12px;
    flex: none;
    fill: var(--brand-red);
  }
  .chat-icon {
    width: 17px;
    height: 17px;
    margin-right: 13px;
    border-radius: 3px;
    background: var(--brand-red);
    flex: none;
  }
  .holder {
    position: absolute;
    right: 60px;
    top: 302px;
    text-align: right;
  }
  .holder-name {
    color: var(--brand-red);
    font-weight: 700;
    font-size: 30px;
    line-height: 34px;
  }
  .holder-title {
    color: var(--text-grey);
    font-size: 21px;
    line-height: 26px;
  }
</style>
</head>
<body>

<section class="card card-front">
  <div class="brand-name">Harbor Lending Circle</div>

  <p class="address">14 Cassia Lane, Suite 310<br>Singapore 047219</p>

  <ul class="contact-list">
    <li>
      <svg class="contact-icon" viewBox="0 0 24 24"><path d="M6.6 10.8c1.4 2.8 3.8 5.1 6.6 6.6l2.2-2.2c.3-.3.7-.4 1-.2 1.1.4 2.3.6 3.6.6.6 0 1 .4 1 1V20c0 .6-.4 1-1 1C10.6 21 3 13.4 3 4c0-.6.4-1 1-1h3.5c.6 0 1 .4 1 1 0 1.3.2 2.5.6 3.6.1.3 0 .7-.2 1z"/></svg>
      +65 555-0142
    </li>
    <li>
      <svg class="contact-icon" viewBox="0 0 24 24"><path d="M2 5h20v14H2z M3.5 6.5l8.5 6.5 8.5-6.5" fill="none" stroke="var(--brand-red)" stroke-width="0"/><path d="M2 5h20v2l-10 6L2 7z"/><path d="M2 9l10 6 10-6v10H2z"/></svg>
      peterwilks@hlc-example.asia
    </li>
    <li>
      <svg class="contact-icon" viewBox="0 0 24 24"><circle cx="12" cy="12" r="10"/><path d="M7 6c2 1 3 3 2 5s1 3 2 5M15 5c-1 2 1 3 3 3M14 14c2 0 3 2 2 4" fill="none" stroke="#fff" stroke-width="1.6" stroke-linecap="round"/></svg>
      www.hlc-example.asia
    </li>
    <li>
      <span class="chat-icon"></span>
      peterwilks
    </li>
  </ul>

  <div class="holder">
    <div class="holder-name">PETER WILKS</div>
    <div class="holder-title">Co-Founder | Partner</div>
  </div>

  <span class="corner-mark"></span>
  <div class="accent-band"></div>
</section>

<section class="card card-back">
  <div class="brand-name">Harbor Lending Circle</div>
  <span class="corner-mark"></span>
  <div class="accent-band"></div>
</section>

</body>
</html>
```